Snack package design "Lantern Curl Bites"

Looking to create a fun package design of snack. Snack is sweet and crunchy; great for people that wants to munch on stuff. Name of the Snack is "Lantern Curl Bites". The net weight should be 16oz (453 grams). I added brand "TWbR" Tiny Wonders bring Rain on the file. I also added picture of the snack. Package will be a pouch type.

Target Market(s)

People that like sweet snacks

Industry/Entity Type

Food snacks

Requirements
Must have
• Name of Snack "Lantern Curl Bites" and logo of company on top left.
Nice to have
• something that's simple and clean design

```html
<!DOCTYPE html>
<html lang="en">
<head>
<meta charset="utf-8">
<title>Lantern Curl Bites – Pouch Front</title>
<link href="https://fonts.googleapis.com/css2?family=Fredoka:wght@700&family=Ubuntu:wght@400&display=swap" rel="stylesheet">
<style>
  :root {
    --canvas: #ffffff;
    --pouch-top: #f1f1f1;
    --pouch-top-edge: #e4e4e4;
    --snack-light: #e29a4e;
    --snack-mid: #c9763a;
    --snack-dark: #9c5424;
    --band-light: #c0913d;
    --band-mid: #9a6a22;
    --band-dark: #5c3a10;
    --title: #efefef;
    --brand: #8a5a1c;
    --netwt: #f2f2f2;
  }
  * { margin: 0; padding: 0; box-sizing: border-box; }
  html, body {
    width: 1200px; height: 1200px; overflow: hidden;
    background: var(--canvas);
  }
  .canvas { position: relative; width: 1200px; height: 1200px; }
  .pouch-front {
    position: absolute; left: 259px; top: 50px;
    width: 682px; height: 1100px;
    background: linear-gradient(180deg, var(--pouch-top) 0%, var(--pouch-top-edge) 35%);
    overflow: hidden;
  }
  .brand-block {
    position: absolute; left: 58px; top: 190px;
    display: flex; align-items: center; gap: 12px;
    font-family: "Fredoka", sans-serif; font-weight: 700;
    color: var(--brand);
  }
  .brand-square {
    width: 22px; height: 22px; background: var(--brand);
  }
  .brand-name { font-size: 30px; line-height: 1; letter-spacing: 0.5px; }
  .snack-photo { position: absolute; left: 0; top: 265px; width: 682px; height: 405px; }
  .title-band { position: absolute; left: 0; top: 0; width: 682px; height: 1100px; }
  .product-title {
    position: absolute; left: 122px; top: 660px;
    font-family: "Fredoka", sans-serif; font-weight: 700;
    font-size: 112px; line-height: 104px; color: var(--title);
    letter-spacing: -1px;
  }
  .net-weight {
    position: absolute; left: 0; right: 0; top: 1008px;
    text-align: center;
    font-family: "Ubuntu", sans-serif; font-size: 17px; color: var(--netwt);
  }
</style>
</head>
<body>
<div class="canvas">
  <section class="pouch-front">
    <div class="brand-block">
      <span class="brand-square"></span>
      <span class="brand-name">TWbR · Tiny Wonders bring Rain</span>
    </div>

    <svg class="snack-photo" viewBox="0 0 682 405" role="img" aria-label="Photo of a heap of golden, crunchy curled snack bites">
      <defs>
        <linearGradient id="snackTone" x1="0" y1="0" x2="0" y2="1">
          <stop offset="0" stop-color="var(--snack-light)"/>
          <stop offset="0.55" stop-color="var(--snack-mid)"/>
          <stop offset="1" stop-color="var(--snack-dark)"/>
        </linearGradient>
      </defs>
      <path d="M0 60 Q60 40 120 48 Q180 42 240 36 Q300 30 360 10 Q420 4 470 18 Q540 20 600 26 Q650 28 682 20 L682 405 L0 405 Z" fill="url(#snackTone)"/>
    </svg>

    <svg class="title-band" viewBox="0 0 682 1100" aria-hidden="true">
      <defs>
        <linearGradient id="bandTone" x1="0" y1="0" x2="0.25" y2="1">
          <stop offset="0" stop-color="var(--band-light)"/>
          <stop offset="0.45" stop-color="var(--band-mid)"/>
          <stop offset="1" stop-color="var(--band-dark)"/>
        </linearGradient>
      </defs>
      <path d="M0 643 Q341 615 682 645 L682 1100 L0 1100 Z" fill="url(#bandTone)"/>
    </svg>

    <h1 class="product-title">Lantern<br>Curl<br>Bites</h1>
    <p class="net-weight">Net Wt. 16oz (453 grams)</p>
  </section>
</div>
</body>
</html>
```